Cat-products company needs smart, yet endearing, business card

We need a business card design for a new, but up-and-running, business based in Honolulu, Hawaii. The business is Purrlane Nest Co. Our first product is the most environmentally-friendly cat grass kit ever seen on the planet. Future products, currently in the R&D phase, will include a variety of exciting cat scratchers. We also do consulting work to help apartment-dwellers make their home more cat-friendly and, in the future, plan on doing full, custom installs of structure to create high walkways for cats.

Target Market(s)

Middle-aged, apartment-dwelling, middle-class workers who own 1 or more cats and who dote on them.

Industry/Entity Type

Pet Care

Contact Information for Business Card

A striking, professional, yet warm and friendly design is what we're after.

Font styles to use
Serif
Sans Serif
Other font styles liked:
• Comfortaa

Colors

Designer to choose colors to be used in the design.

Requirements
Must have
• The company logo: (see attachment)
• The company name: Purrlane Nest Co
• The web address: www.purrlanenestco.example
• Email: support@purrlanenestco.example
• Phone: +1 (808) 555 0172
• Update (Fri Jun 30 3017 7:45pm Hawaii Time) I would like, is possible, uploaded picture of the cat grass kit on the back of the card with some text along the lines of: Purrlane Nest Co - Where The Freshest Kitty Sprouts Begin
Nice to have
• A cat picture, cartoon, real or silhouette that illustrates cats in action and/or relaxing; ie using the apartment space to live, play and relax in and being well-contented.
• Most of the website is done in the font: Comfortaa. It might be nice to continue using this for brand consistency.
Should not have
• Hard-to-read fonts.

```html
<!DOCTYPE html>
<html lang="en">
<head>
<meta charset="utf-8">
<title>Purrlane Nest Co – Business Card</title>
<link rel="stylesheet" href="https://fonts.googleapis.com/css2?family=Oswald:wght@600&family=Jost:wght@400;500;600&display=swap">
<style>
  :root {
    --stage: #2a2a2a;
    --card: #232323;
    --card-edge: #1b1b1b;
    --ink-light: #f4f4f4;
    --ink-muted: #6f6f6f;
    --accent: #f2a51d;
    --divider: #9a9a9a;
  }
  * { box-sizing: border-box; margin: 0; padding: 0; }
  html, body {
    width: 1200px; height: 1000px; overflow: hidden;
    background: var(--stage);
  }
  .stage {
    width: 1200px; height: 1000px;
    display: flex; flex-direction: column;
    align-items: center; justify-content: center; gap: 60px;
  }
  .card {
    width: 700px; height: 400px;
    background: var(--card);
    border: 1px solid var(--card-edge);
    box-shadow: 0 14px 30px rgba(0,0,0,.45);
    position: relative;
  }
  /* Front */
  .card--front {
    display: flex; align-items: center; justify-content: center; gap: 14px;
  }
  .brand-dot {
    width: 26px; height: 26px; border-radius: 50%;
    background: var(--ink-muted);
  }
  .brand-name {
    font-family: "Jost", sans-serif; font-weight: 600;
    font-size: 42px; color: var(--ink-muted); letter-spacing: .5px;
  }
  /* Back */
  .identity {
    position: absolute; top: 150px; right: 380px; text-align: right;
  }
  .identity__name {
    font-family: "Oswald", sans-serif; font-weight: 600;
    font-size: 36px; line-height: 1.1; color: var(--ink-light);
    letter-spacing: 1px;
  }
  .identity__role {
    font-family: "Jost", sans-serif; font-weight: 600;
    font-size: 20px; color: var(--accent);
  }
  .divider {
    position: absolute; top: 150px; left: 340px;
    width: 1px; height: 70px; background: var(--divider);
  }
  .contacts {
    position: absolute; top: 150px; left: 360px;
    list-style: none;
    font-family: "Jost", sans-serif; font-size: 17px; color: var(--ink-light);
  }
  .contacts li { display: flex; align-items: center; gap: 12px; height: 23px; }
  .contacts svg { width: 15px; height: 15px; flex: none; }
  .contacts .highlight { color: var(--accent); }
  .address {
    position: absolute; left: 40px; bottom: 50px;
    display: flex; align-items: center; gap: 12px;
    font-family: "Jost", sans-serif; font-size: 18px; color: var(--ink-light);
    letter-spacing: .6px;
  }
  .address svg { width: 16px; height: 20px; }
</style>
</head>
<body>
<main class="stage">
  <section class="card card--front" aria-label="Card front">
    <span class="brand-dot"></span>
    <span class="brand-name">Purrlane Nest Co</span>
  </section>

  <section class="card card--back" aria-label="Card back">
    <div class="identity">
      <p class="identity__name">KALANI BROOKS</p>
      <p class="identity__role">Director</p>
    </div>
    <span class="divider"></span>
    <ul class="contacts">
      <li>
        <svg viewBox="0 0 16 16" aria-hidden="true"><path fill="#f2a51d" d="M3 1l3 3-2 2c1 2 3 4 5 5l2-2 3 3-2 2C7 14 2 9 1 3z"/></svg>
        +1 (808) 555 0172
      </li>
      <li>
        <svg viewBox="0 0 16 16" aria-hidden="true"><rect x="1" y="3" width="14" height="10" fill="#f2a51d"/><path d="M1 3l7 6 7-6" fill="none" stroke="#232323" stroke-width="1.3"/></svg>
        support@purrlanenestco.example
      </li>
      <li>
        <svg viewBox="0 0 16 16" aria-hidden="true"><g fill="none" stroke="#f2a51d" stroke-width="1.2"><circle cx="8" cy="8" r="6.5"/><ellipse cx="8" cy="8" rx="3" ry="6.5"/><path d="M1.5 8h13M2.5 4.5h11M2.5 11.5h11"/></g></svg>
        <span>www.<span class="highlight">purrlanenestco</span>.example</span>
      </li>
    </ul>
    <p class="address">
      <svg viewBox="0 0 16 20" aria-hidden="true"><path fill="#f2a51d" d="M8 0a7 7 0 0 1 7 7c0 5-7 13-7 13S1 12 1 7a7 7 0 0 1 7-7z"/><circle cx="8" cy="7" r="2.6" fill="#232323"/></svg>
      Your Street Address Here, Country Name, 1234
    </p>
  </section>
</main>
</body>
</html>
```